Business card design

I need my logo on this card, things I need the card to have on it
licensed and insured.
owner operators Derek & Milton Halvorsen
my phone number 5418237906
Disaster Recovery, Storm Damage Restoration, Proactive Disaster Plan Management, Roof Repair/Restoration Structural Repair and Reconstruction, Emergency Boarding and Tarping Service, Perimeter Fencing, Emergency Tree Removal,

```html
<!DOCTYPE html>
<html lang="en">
<head>
<meta charset="utf-8">
<title>Halvorsen's Construction – Business Card</title>
<link href="https://fonts.googleapis.com/css2?family=Lato:wght@400&display=swap" rel="stylesheet">
<style>
  :root {
    --page: #ece8e2;
    --card-blue: #3a6fd9;
    --card-blue-deep: #3366d2;
    --ink: #ffffff;
    --photo-sky: #d9d6c8;
    --photo-mid: #9a8f78;
    --photo-ground: #5e5446;
    --shadow: rgba(40, 35, 30, 0.22);
  }
  * { box-sizing: border-box; margin: 0; padding: 0; }
  html, body {
    width: 1200px;
    height: 800px;
    overflow: hidden;
    background: var(--page);
    font-family: "Lato", "Gill Sans", sans-serif;
    color: var(--ink);
  }
  .sheet {
    width: 1200px;
    height: 800px;
    display: flex;
    align-items: center;
    justify-content: center;
    gap: 44px;
  }
  .card {
    position: relative;
    width: 540px;
    height: 309px;
    background: var(--card-blue);
    box-shadow: 0 10px 28px var(--shadow);
    overflow: hidden;
  }

  /* Front */
  .card-front .blue-panel {
    position: absolute;
    left: 0; top: 0;
    width: 292px;
    height: 100%;
    padding: 30px 0 0 36px;
  }
  .brand {
    display: flex;
    align-items: center;
    gap: 10px;
  }
  .brand-square {
    width: 22px;
    height: 22px;
    background: var(--ink);
  }
  .brand-text { line-height: 1; }
  .brand-name {
    font-size: 19px;
    letter-spacing: 0.5px;
  }
  .brand-sub {
    margin-top: 4px;
    font-size: 6.5px;
    letter-spacing: 3px;
  }
  .services {
    list-style: none;
    position: absolute;
    left: 36px;
    bottom: 28px;
    font-size: 11.6px;
    line-height: 1.42;
    letter-spacing: 0.15px;
  }
  .photo {
    position: absolute;
    right: 0; top: 0;
    width: 248px;
    height: 100%;
    background:
      radial-gradient(circle at 22% 14%, rgba(255,255,250,0.85) 0, rgba(255,255,250,0) 32%),
      linear-gradient(180deg, var(--photo-sky) 0%, var(--photo-mid) 55%, var(--photo-ground) 100%);
  }

  /* Back */
  .card-back {
    display: flex;
    flex-direction: column;
    align-items: center;
    justify-content: center;
    text-align: center;
    background: linear-gradient(135deg, var(--card-blue-deep), var(--card-blue));
  }
  .back-name {
    font-size: 44px;
    letter-spacing: 1.5px;
    line-height: 1;
  }
  .back-sub {
    margin-top: 6px;
    font-size: 11px;
    letter-spacing: 9px;
    padding-left: 9px;
  }
  .owners {
    margin-top: 26px;
    font-size: 17px;
    letter-spacing: 0.3px;
  }
  .phone {
    margin-top: 4px;
    font-size: 17px;
    letter-spacing: 0.3px;
  }
</style>
</head>
<body>
<main class="sheet">
  <section class="card card-front">
    <div class="blue-panel">
      <div class="brand">
        <span class="brand-square"></span>
        <div class="brand-text">
          <div class="brand-name">HALVORSEN'S</div>
          <div class="brand-sub">CONSTRUCTION L.L.C</div>
        </div>
      </div>
      <ul class="services">
        <li>Disaster Recovery</li>
        <li>Perimeter Fencing</li>
        <li>Emergency Tree Removal</li>
        <li>Roof Repair/Restoration</li>
        <li>Storm Damage Restoration</li>
        <li>Proactive Disaster Plan Management</li>
        <li>Structural Repair and Reconstruction</li>
        <li>Emergency Boarding and Tarping Service</li>
      </ul>
    </div>
    <div class="photo" role="img" aria-label="Photo of two construction workers in hard hats and safety vests overlooking a sunlit building site with cranes"></div>
  </section>

  <section class="card card-back">
    <div class="back-name">HALVORSEN'S</div>
    <div class="back-sub">CONSTRUCTION L.L.C</div>
    <p class="owners">Derek &amp; Milton Halvorsen</p>
    <p class="phone">P: 541-823-7906</p>
  </section>
</main>
</body>
</html>
```